Tidewell Marketing company is looking for a web page design

Your projects should contain:

1. Header: Logo provided by us.
2. Top nav bar: offer, about us, experience, contact.
3. “Choose language” button.
4. Main section: panoramic picture (static, professional, modern).
5. Below section: 3 blocks (image+title+description), which represent our 3 main activities (titles):
• Market Research,
• Marketing Plans,
• Marketing Project.
6. ‘Contact us’ form – Message (text: “Write your message and give us details about your company and activities”), Email, SEND).
7. Page footer: (4 section: Contact, Social Media, Blog, Partners).
Updates

Hello!

I uploaded new file 'general_look', which is our idea how the page should generally look like.

BUT! it doesn't mean that your projects should look exactly like this project e.g.:
* titles Market Research, Marketing Plans, Marketing Project can be above these: Image 1,2,3.
* everything doesn't have to be in square and rectangle shape. You can try to manipulate with blocks and can add elipse elemnts or something similar.

We will appreciate your innovative ideas. Just wanted to give you general plan of the site and ilustrate all elements that we require.

Best Regards,
Benedek

IMPORTENT

Please remember that the main picture should be panoramic. Please do not close it in frame.

Target Market(s)

Small and middle sized companies, which would like to export their goods and services abroad and are interested in raising funds from Northgate Trade Council to expand their activities. These are rather industrial companies with low level of innovativeness. Our mission is to build image of the client’s company and increase awareness of their products to improve their competitiveness and innovativeness.

Industry/Entity Type

It Company

Requirements
Must have
• 1. Create designs of main page and subpage.
2. Subpage: Logo, Header, language button, place for article, navigation menu on the right side - below it “contact us” button , footer on the bottom. (In this section we are looking mainly for the design of the header and navigation menu).
3. The whole design should be a series of horizontal blocks.
4. Your projects should be associated with features such as: Reliability, Security, Professionalism, Openness, Uniqueness.
5. The design should be simple, fresh, readable, easy to use and should create a feeling of high quality services.
6. Possibility to change the panoramic picture (separate layer in a graphic file).
7. All pictures and blocks should be static, no movements.
8. Style of the page should be compliant with the logo design, font: Swiss.
9. Designs that we like: http://www.fernvale-studio.pl/, http://www.plumquarry.com/.
Should not have
• There shouldn’t be any distractions and not matching parts (whole design should be compact and easy to interpret and remember).

```html
<!DOCTYPE html>
<html lang="en">
<head>
<meta charset="utf-8">
<title>Tidewell Marketing</title>
<link href="https://fonts.googleapis.com/css2?family=Jost:wght@400;500&family=Arimo:wght@400;700&display=swap" rel="stylesheet">
<style>
:root{
  --brand:#2f84ad;
  --brand-dark:#1c5f86;
  --ink:#333;
  --muted:#666;
  --heading:#2a2a2a;
  --band:#f4f4f4;
  --line:#b8b8b8;
  --hero-a:#ffffff;
  --hero-b:#d6e5ef;
  --link:#1e6f9c;
  --navy:#14287a;
}
*{box-sizing:border-box;margin:0;padding:0}
html,body{width:997px;height:1200px;overflow:hidden;background:#fff}
body{position:relative;font-family:"Arimo",Arial,sans-serif;color:var(--ink)}
.abs{position:absolute}
.top-bar{left:83px;top:0;width:831px;height:7px;background:var(--brand);border-radius:0 0 5px 5px}
.quick-call{left:97px;top:43px;font-size:10px;color:#000}
.quick-call span{color:var(--brand);font-style:italic;font-size:12px}
.lang-select{left:734px;top:43px;width:168px;height:20px;border:1px solid #b9c7d2;background:#eef3f6;font-size:10px;padding:4px 7px;color:#111}
.lang-select i{position:absolute;right:2px;top:2px;width:15px;height:14px;background:#333}
.lang-select i::after{content:"";position:absolute;left:4px;top:4px;border:4px solid transparent;border-top:5px solid #fff}
.logo{left:91px;top:98px;display:flex;align-items:center;gap:8px;font-family:"Jost",sans-serif;font-weight:500;font-size:31px;color:var(--brand-dark);letter-spacing:-.5px}
.logo b{display:block;width:40px;height:40px;border-radius:50%;background:var(--brand-dark)}
.main-nav a{position:absolute;top:115px;font-family:"Jost",sans-serif;font-size:13.5px;color:#333;text-decoration:none}
.hero{left:0;top:162px;width:997px;height:335px;background:linear-gradient(180deg,var(--hero-a) 0%,var(--hero-b) 100%)}
.hero-photo{position:absolute;left:125px;top:46px;width:473px;height:274px;border-radius:40px;background:radial-gradient(ellipse at 50% 55%,#eef2f6 0%,#c9d8e4 60%,rgba(214,229,239,0) 100%)}
.hero-copy{position:absolute;left:675px;top:117px;font-family:"Jost",sans-serif;font-size:21px;line-height:30px;color:#555;width:220px}
.hero-btn{position:absolute;left:674px;top:248px;width:125px;height:34px;background:#4e8eb5;color:#fff;font-family:"Jost",sans-serif;font-size:15.5px;line-height:34px;text-align:center;border-radius:2px}
.band{left:0;top:497px;width:997px;height:268px;background:var(--band)}
.dots{position:absolute;left:451px;top:13px;display:flex;gap:6px}
.dots i{width:11px;height:11px;border-radius:50%;border:1px solid #bbb;background:#fff}
.dots i.on{background:#555;border-color:#555}
.activity{position:absolute;top:42px;width:225px}
.activity h2{font-family:"Jost",sans-serif;font-weight:400;font-size:15px;color:var(--heading)}
.activity .pic{width:78px;height:72px;margin:10px 0 14px 6px;border-radius:8px}
.activity p{font-size:10px;line-height:16.6px;color:var(--muted)}
.activity a{display:inline-block;margin-top:14px;font-size:10px;color:var(--link)}
.divider{position:absolute;top:50px;width:1px;height:180px;background:linear-gradient(#f4f4f4,#d8d8d8,#f4f4f4)}
.enquiry{left:106px;top:784px;width:784px;height:173px;border:1px solid var(--line);border-radius:3px;background:linear-gradient(180deg,#fff 60%,#f1f1f1)}
.enquiry-copy{position:absolute;left:15px;top:24px;width:310px;font-family:"Jost",sans-serif;font-size:15px;line-height:18px;color:var(--brand)}
.enquiry-copy p+p{margin-top:18px}
.field{position:absolute;border:1px solid #888;background:#fff;font-size:11px;color:#999;padding:8px 13px}
.send{position:absolute;left:363px;top:138px;font-family:"Arimo",sans-serif;font-size:15px;color:var(--navy);text-decoration:underline}
.footer-mark{left:102px;top:996px;width:40px;height:40px;border-radius:50%;background:var(--brand-dark)}
.footer-col{position:absolute;top:1013px}
.footer-col h3{font-family:"Jost",sans-serif;font-weight:400;font-size:15px;color:var(--heading);margin-bottom:14px}
.footer-list{font-size:10px;line-height:15px;color:var(--muted);letter-spacing:.3px}
.address{left:103px;top:1046px}
.blog strong{display:block;font-size:10.5px;color:#555;line-height:11px}
.blog p{font-size:10px;line-height:11.7px;color:var(--muted);width:130px}
.social{display:flex;gap:9px;margin-left:2px}
.social i{width:21px;height:21px;border-radius:50%}
</style>
</head>
<body>
<div class="abs top-bar"></div>
<div class="abs quick-call">For Quick response u can call us at: <span>020 555 0187</span></div>
<div class="abs lang-select">Select Language<i></i></div>
<div class="abs logo"><b></b>Tidewell Marketing</div>
<nav class="main-nav">
  <a style="left:510px">OFFER</a>
  <a style="left:600px">ABOUT US</a>
  <a style="left:720px">EXPERIENCE</a>
  <a style="left:839px">CONTACT</a>
</nav>

<section class="abs hero">
  <div class="hero-photo" role="img" aria-label="Panoramic photo of two businessmen reviewing a document at a laptop"></div>
  <p class="hero-copy">See how we provide innovative services to your business with economical price</p>
  <div class="hero-btn">Contact Us Now</div>
</section>

<section class="abs band">
  <div class="dots"><i class="on"></i><i></i><i></i><i></i></div>
  <div class="activity" style="left:111px">
    <h2>MARKET RESEARCH</h2>
    <div class="pic" role="img" aria-label="Magnifying glass over a bar chart" style="background:radial-gradient(circle at 40% 40%,#e2f4f4,#9ab 70%,#f4f4f4 72%)"></div>
    <p>some lorem ipsum text will be here some lorem ipsum text will be here some lorem ipsum text will be here some lorem ipsum text will be here some lorem ipsum text will be here</p>
    <a>read more</a>
  </div>
  <div class="divider" style="left:357px"></div>
  <div class="activity" style="left:395px">
    <h2>MARKETING PLANS</h2>
    <div class="pic" role="img" aria-label="Silhouette of a head filled with marketing words" style="background:linear-gradient(135deg,#2b2b2b,#111)"></div>
    <p>some lorem ipsum text will be here some lorem ipsum text will be here some lorem ipsum text will be here some lorem ipsum text will be here some lorem ipsum text will be here</p>
    <a>read more</a>
  </div>
  <div class="divider" style="left:638px"></div>
  <div class="activity" style="left:670px">
    <h2>MARKETING PROJECT</h2>
    <div class="pic" role="img" aria-label="Orange folder with project documents" style="background:linear-gradient(160deg,#f0a640,#b86a14)"></div>
    <p>some lorem ipsum text will be here some lorem ipsum text will be here some lorem ipsum text will be here some lorem ipsum text will be here some lorem ipsum text will be here</p>
    <a>read more</a>
  </div>
</section>

<section class="abs enquiry">
  <div class="enquiry-copy">
    <p>Are your looking for marketing service for your business, Just fill the form and we will get back to you as soon as possible.</p>
    <p>Our mission is to build image of the client’s company and increase awareness of their products to improve their competitiveness and innovativeness.</p>
  </div>
  <div class="field" style="left:359px;top:28px;width:189px;height:30px">Your Name</div>
  <div class="field" style="left:559px;top:28px;width:189px;height:30px">Your Email id</div>
  <div class="field" style="left:360px;top:70px;width:388px;height:57px">Message</div>
  <a class="send">Send</a>
</section>

<div class="abs footer-mark"></div>
<div class="footer-col footer-list address">Tidewell Marketing Inc.<br>14, Harbour Row,<br>Leeds<br>UK<br>Call: 020 555 0187<br>Email: info@tidewellmarketing.com</div>
<div class="footer-col" style="left:306px"><h3>ABOUT US</h3></div>
<div class="footer-col footer-list" style="left:303px;top:1046px">About Us<br>Careers<br>For the Press<br>Terms of Use<br>Privacy</div>
<div class="footer-col" style="left:456px"><h3>SERVICES</h3></div>
<div class="footer-col footer-list" style="left:454px;top:1046px">Services details<br>Services details here<br>Services details<br>Services details<br>here details<br>Services details<br>Services details</div>
<div class="footer-col blog" style="left:615px"><h3>BLOG</h3></div>
<div class="footer-col blog" style="left:613px;top:1047px"><strong>Latest Articles heading</strong><p>some text will be here some text will be here some text will be here some text will be here some text will be here</p></div>
<div class="footer-col" style="left:807px"><h3>FOLLOW US</h3>
  <div class="social"><i style="background:#3a3a3a"></i><i style="background:#34aee8"></i><i style="background:#3b5a98"></i></div>
</div>
</body>
</html>
```